Velvet Shakers business card

We would like a business card designed for our business velvet shakers

We need it to have 2 sides.

More information about the business can be found at www.velvetshakers-example.net

Industry/Entity Type

Business

```html
<!DOCTYPE html>
<html lang="en">
<head>
<meta charset="utf-8">
<title>Velvet Shakers – Business Card</title>
<link rel="stylesheet" href="https://fonts.googleapis.com/css2?family=Lobster&family=Montserrat:wght@400;500;700&display=swap">
<style>
  :root {
    --bg: #3a3a3c;
    --card-dark: #1f1b19;
    --card-dark-edge: #2a2522;
    --card-light: #ffffff;
    --ink: #1d1d1d;
    --ink-soft: #3b3b3b;
    --gold: #c9a85a;
    --gold-light: #ead7a0;
    --swoosh-dark: #161311;
  }
  * { margin: 0; padding: 0; box-sizing: border-box; }
  html, body { width: 1200px; height: 852px; overflow: hidden; }
  body {
    background: var(--bg);
    display: flex;
    align-items: center;
    justify-content: center;
    gap: 40px;
    font-family: "Montserrat", sans-serif;
  }
  .card {
    position: relative;
    width: 540px;
    height: 310px;
    border-radius: 22px;
    overflow: hidden;
  }
  .card-front {
    background: radial-gradient(ellipse at 40% 45%, var(--card-dark-edge), var(--card-dark) 70%);
    display: flex;
    align-items: center;
    justify-content: center;
  }
  .front-wordmark {
    font-family: "Montserrat", sans-serif;
    font-weight: 700;
    font-size: 46px;
    letter-spacing: 0.5px;
    color: var(--gold);
  }
  .card-back { background: var(--card-light); }
  .back-wordmark {
    position: absolute;
    left: 30px;
    top: 212px;
    font-family: "Montserrat", sans-serif;
    font-weight: 700;
    font-size: 24px;
    color: var(--ink);
  }
  .contact-block {
    position: absolute;
    left: 246px;
    top: 36px;
    color: var(--ink-soft);
    font-size: 11.5px;
    line-height: 1.45;
  }
  .person-name {
    font-family: "Lobster", cursive;
    font-size: 28px;
    color: var(--ink);
    line-height: 1;
  }
  .person-role { margin-bottom: 14px; }
  .address { margin-bottom: 12px; margin-left: 14px; }
  .contact-list { list-style: none; margin-left: 20px; }
  .contact-list li { display: flex; align-items: center; gap: 8px; white-space: nowrap; }
  .contact-list svg { width: 11px; height: 11px; flex: none; fill: var(--ink); }
  .swoosh { position: absolute; left: 0; bottom: 0; width: 540px; height: 310px; }
</style>
</head>
<body>
  <section class="card card-front" aria-label="Card front">
    <span class="front-wordmark">Velvet Shakers</span>
  </section>

  <section class="card card-back" aria-label="Card back">
    <svg class="swoosh" viewBox="0 0 540 310" aria-hidden="true">
      <defs>
        <linearGradient id="goldBand" x1="0" y1="1" x2="1" y2="0">
          <stop offset="0" stop-color="#c9a85a"/>
          <stop offset="0.5" stop-color="#ead7a0"/>
          <stop offset="1" stop-color="#c9a85a"/>
        </linearGradient>
      </defs>
      <path d="M150 310 C 330 300, 470 262, 540 215 L540 310 Z" fill="url(#goldBand)"/>
      <path d="M175 310 C 350 300, 480 265, 540 238 L540 310 Z" fill="var(--swoosh-dark)"/>
      <path d="M300 310 C 420 302, 500 282, 540 262 L540 310 Z" fill="url(#goldBand)"/>
      <path d="M320 310 C 430 304, 505 290, 540 276 L540 310 Z" fill="var(--card-light)"/>
    </svg>

    <span class="back-wordmark">Velvet Shakers</span>

    <div class="contact-block">
      <p class="person-name">Marcus</p>
      <p class="person-role">Cocktail Maker</p>
      <p class="address">PO Box 4410 Harbourside<br>Queensland, Australia</p>
      <ul class="contact-list">
        <li><svg viewBox="0 0 12 12"><path d="M2.5 1 L4.5 1 L5.2 3.6 L4 4.6 C4.6 6 6 7.4 7.4 8 L8.4 6.8 L11 7.5 L11 9.5 C11 10.3 10.3 11 9.5 11 C5 11 1 7 1 2.5 C1 1.7 1.7 1 2.5 1 Z"/></svg>0491570110 or 0491570111</li>
        <li><svg viewBox="0 0 12 12"><circle cx="6" cy="6" r="5"/></svg>/velvetshakers-example.net</li>
        <li><svg viewBox="0 0 12 12"><path d="M1 2.5 H11 V9.5 H1 Z M1.8 3.2 L6 6.5 L10.2 3.2" stroke="#fff" stroke-width="0.8"/></svg>info@velvetshakers-example.net</li>
        <li><svg viewBox="0 0 12 12"><circle cx="6" cy="6" r="5"/><path d="M1 6 H11 M6 1 C3.5 3.5 3.5 8.5 6 11 M6 1 C8.5 3.5 8.5 8.5 6 11" stroke="#fff" stroke-width="0.7" fill="none"/></svg>www.velvetshakers-example.net</li>
      </ul>
    </div>
  </section>
</body>
</html>
```